Tessel Vodka bottle label for grassroots distiller, micro-distiller in Kansas. Quillan Forge Distilli

We are located in South Central Kansas. Needing a design for a vodka label. The vodka will be distilled using white milo, which has not been done in the US as far as we know. We are in Kansas and a true "grass roots" business. We are starting on a shoestring, using bare essentials, and locally sourced components. We are looking for a clean, eye catching, grass roots feel. We also will be able to label it non gmo and Gluten free.

Target Market(s)

Upper mid-range price point. Target audience is professionals 25-50 with discretionary income and descerning taste.

Logo Text

Tessel Vodka, Sorghum Based Vodka. Non GMO, AND GLUTEN FREE. Quillan Forge Distilling, 847 W. 3rd Avenue, Kinsley, Ks.

Other font styles liked:
• Georgia, does not have to be, open

Colors
000000

Requirements
Must have
• Simple. Clean. And comply with PQX regulations for labeling found at www.PQX-regs.example
Nice to have
• Stylized image of White Milo. Proundly made in South Central Kansas with locally sourced grain.
Should not have
• Too many words. Exclusively Kansas.

```html
<!DOCTYPE html>
<html lang="en">
<head>
<meta charset="utf-8">
<title>Tessel Vodka — Bottle Label</title>
<link rel="stylesheet" href="https://fonts.googleapis.com/css2?family=Cormorant+SC:wght@500;600&family=Bodoni+Moda:wght@500&display=swap">
<style>
  :root {
    --backdrop: #a99c85;
    --label-paper: #fbfbfb;
    --label-paper-shade: #ececec;
    --band-grey: #d9d9d9;
    --ink: #111111;
    --ink-soft: #2a2a2a;
    --field-light: #e4e4e4;
    --field-mid: #b9b9b9;
    --ground-dark: #161616;
    --windmill-dark: #1c1c1c;
    --windmill-rust: #5a2a22;
  }
  html, body {
    margin: 0;
    width: 1200px;
    height: 1200px;
    overflow: hidden;
    background: var(--backdrop);
  }
  .label {
    position: absolute;
    left: 270px;
    top: 158px;
    width: 660px;
    height: 884px;
    overflow: hidden;
    border-radius: 50% 50% 0 0 / 30% 30% 0 0;
    background: linear-gradient(180deg, var(--label-paper) 0%, var(--label-paper) 55%, var(--label-paper-shade) 100%);
  }
  .claim-band {
    position: absolute;
    left: 0;
    top: 86px;
    width: 100%;
    height: 47px;
    background: var(--band-grey);
  }
  .claim-band__text {
    margin: 0;
    line-height: 47px;
    text-align: center;
    font-family: "Cormorant SC", Georgia, serif;
    font-weight: 600;
    font-size: 33px;
    letter-spacing: 1px;
    color: var(--ink-soft);
  }
  .origin-line {
    position: absolute;
    left: 0;
    top: 138px;
    width: 100%;
    margin: 0;
    text-align: center;
    font-family: "Cormorant SC", Georgia, serif;
    font-weight: 600;
    font-size: 26px;
    letter-spacing: 1.5px;
    word-spacing: 6px;
    color: var(--ink);
  }
  .prairie-art {
    position: absolute;
    left: 0;
    top: 360px;
    width: 100%;
    height: 524px;
    background: linear-gradient(180deg,
      rgba(255,255,255,0) 0%,
      rgba(236,236,236,0.6) 50%,
      var(--field-light) 60%,
      var(--field-mid) 86%,
      var(--ground-dark) 93%,
      var(--ground-dark) 100%);
  }
  .windmill-art {
    position: absolute;
    left: 156px;
    top: 355px;
    width: 176px;
    height: 480px;
    border-radius: 88px 88px 4px 4px;
    background: linear-gradient(180deg,
      var(--windmill-dark) 0%,
      rgba(28,28,28,0.75) 30%,
      rgba(90,42,34,0.55) 65%,
      var(--windmill-dark) 100%);
    opacity: 0.8;
  }
  .product-name {
    position: absolute;
    left: 310px;
    top: 468px;
    margin: 0;
    color: var(--ink);
  }
  .product-name__grain {
    display: block;
    margin-left: 50px;
    font-family: "Cormorant SC", Georgia, serif;
    font-weight: 600;
    font-size: 34px;
    letter-spacing: 1px;
    line-height: 1;
  }
  .product-name__spirit {
    display: block;
    font-family: "Bodoni Moda", Georgia, serif;
    font-weight: 500;
    font-size: 78px;
    letter-spacing: 4px;
    line-height: 1;
    margin-top: 2px;
  }
</style>
</head>
<body>
  <main class="label">
    <div class="prairie-art" role="img" aria-label="Pencil-style Kansas prairie field with a dark silhouette of farm buildings along the horizon"></div>
    <div class="windmill-art" role="img" aria-label="Tall farm windmill with a fan wheel and tail vane on a lattice tower"></div>
    <div class="claim-band">
      <p class="claim-band__text">Non GMO Gluten Free</p>
    </div>
    <p class="origin-line">Small Batch Product of Kansas USA</p>
    <h1 class="product-name">
      <span class="product-name__grain">White Tessel</span>
      <span class="product-name__spirit">VODKA</span>
    </h1>
  </main>
</body>
</html>
```